Etikettendesign für eine Grillsauce gesucht
Zielgruppe
Genuss aus dem Herzen der Schweiz
Kräuterbutter für Feinschmecker – dafür steht die Hubertsen’s Feinkost AG seit vielen Jahren. Mitten aus dem grünen Herzen der Schweiz verkündet die Hubertsen’s Feinkost AG ihre Genussbotschaft:
Der sorgsame Umgang mit den Rohstoffen der Natur ist die Grundlage für hochwertigen Genuss und vollmundigen Geschmack.
In jedem Produkt der Hubertsen’s Feinkost AG schmeckt man den Einklang mit der Natur: aromatisch, harmonisch, ausgewogen.
Aufgabenstellung
Eine neues Produkt soll entstehen.
- eine Grillsauce. Produktetikett für eine Flasche mit 500ml (welche noch nicht definiert ist) Es handelt sich hier um eine Lebensmitteletikette. Produktangaben wie Inhalte und Nährwerte werden auf dem Rücketikett stehen.
Wir brauchen das Designe für die Frontetikette.
Gestartet wird mit einer Sauce. Weitere Saucen sollen dann folgen.
- Lindo Sauce
- Chimichurri
- Café de Paris
- BBQ
Wir sind noch total in der Findung für ein neues Design. Was wir suchen ist ein Design welches sehr edel daher kommt und Lust auf mehr macht. Die Zielgruppe wird eher der Fleischkonsument und der Grillmeister sein.
Es darf im Vintage stil sein, soll aber elegant und edel wirken.
Es soll in Richtung Lifestyle Produkt gehen, welches der Metzger gerne in seinem Regal stehen hat oder das BBQ Restaurant auf den Tisch stellen will.
Eine Idee z.b. wäre, dass wir alle Saucen in die Roten Ketchup Quetflaschen abfüllen um ein alleinstellungsmerkmal zu haben.

```html
<!DOCTYPE html>
<html lang="de">
<head>
<meta charset="utf-8">
<title>Hubertsen's Saucen – Frontetiketten</title>
<link href="https://fonts.googleapis.com/css2?family=Open+Sans:wght@600;700&family=PT+Sans+Narrow&family=Cousine&display=swap" rel="stylesheet">
<style>
  :root {
    --bg: #efe9e1;
    --tan: #b8906a;
    --tan-text: #c79c6e;
    --black: #0b0808;
    --red: #e41c24;
    --white: #ffffff;
    --bbq: #7a3a1c;
    --lindo: #a8101e;
    --chimi: #0c6b38;
  }
  html, body {
    margin: 0;
    padding: 0;
    width: 1200px;
    height: 890px;
    overflow: hidden;
    background: var(--bg);
  }
  .range {
    position: relative;
    width: 1200px;
    height: 890px;
    display: flex;
    justify-content: center;
    align-items: center;
    gap: 50px;
  }
  .label-slot {
    width: 340px;
    height: 616px;
    position: relative;
  }
  .label {
    position: absolute;
    top: 0;
    left: 0;
    width: 400px;
    height: 725px;
    transform: scale(0.85);
    transform-origin: 0 0;
  }
  .label-shape {
    position: absolute;
    inset: 0;
  }
  .line {
    position: absolute;
    left: 0;
    width: 100%;
    text-align: center;
    margin: 0;
  }
  .sauce-kind {
    top: 50px;
    font-family: "Open Sans", sans-serif;
    font-weight: 700;
    font-size: 31px;
    letter-spacing: 1px;
    color: var(--tan-text);
  }
  .sauce-name {
    top: 100px;
    font-family: "Open Sans", sans-serif;
    font-weight: 600;
    font-size: 92px;
    line-height: 1;
    letter-spacing: 3px;
    color: var(--white);
  }
  .sauce-name--mono {
    top: 98px;
    font-family: "Cousine", monospace;
    font-weight: 400;
    font-size: 50px;
    line-height: 0.95;
    letter-spacing: 2px;
  }
  .brand-name {
    top: 318px;
    font-family: "Open Sans", sans-serif;
    font-weight: 600;
    font-size: 44px;
    line-height: 1;
    color: var(--white);
    letter-spacing: 1px;
  }
  .pairing {
    top: 505px;
    font-family: "Open Sans", sans-serif;
    font-weight: 700;
    color: var(--tan-text);
    line-height: 1.15;
  }
  .pairing-lead { font-size: 24px; display: block; }
  .pairing-detail { font-size: 19px; display: block; }
  .net-weight {
    top: 604px;
    font-family: "PT Sans Narrow", sans-serif;
    font-size: 22px;
    line-height: 1.1;
    color: var(--tan-text);
  }
</style>
</head>
<body>
<main class="range">

  <!-- BBQ -->
  <div class="label-slot">
    <article class="label">
      <svg class="label-shape" viewBox="0 0 400 725" width="400" height="725" aria-hidden="true">
        <defs>
          <radialGradient id="fill-bbq" cx="50%" cy="45%" r="60%">
            <stop offset="0" stop-color="var(--bbq)"/>
            <stop offset="0.8" stop-color="var(--bbq)"/>
            <stop offset="1" stop-color="#3a1a0c"/>
          </radialGradient>
        </defs>
        <path fill="var(--tan)" d="M10,120 C30,30 120,0 200,0 C280,0 370,30 390,120 C405,200 380,250 385,300 L385,380 C400,450 400,520 395,560 C385,660 300,725 200,725 C100,725 15,660 5,560 C0,520 0,450 15,380 L15,300 C20,250 -5,200 10,120 Z"/>
        <rect x="20" y="240" width="360" height="158" fill="var(--red)"/>
        <path fill="var(--black)" d="M20,125 C40,40 125,10 200,10 C275,10 360,40 380,125 C392,190 375,240 375,262 C320,295 260,302 200,302 C140,302 80,295 25,262 C25,240 8,190 20,125 Z"/>
        <path fill="none" stroke="var(--tan)" stroke-width="4" d="M65,215 Q200,285 335,215"/>
        <path fill="var(--black)" d="M20,435 C30,398 100,390 200,390 C300,390 370,398 380,435 C395,520 390,590 370,632 C340,692 280,715 200,715 C120,715 60,692 30,632 C10,590 5,520 20,435 Z"/>
        <ellipse cx="200" cy="565" rx="150" ry="138" fill="url(#fill-bbq)"/>
        <circle cx="200" cy="422" r="58" fill="var(--white)"/>
        <circle cx="200" cy="422" r="48" fill="none" stroke="var(--red)" stroke-width="4"/>
      </svg>
      <p class="line sauce-kind">SAUSE</p>
      <p class="line sauce-name">BBQ</p>
      <p class="line brand-name">hubertsen's</p>
      <p class="line pairing"><span class="pairing-lead">PERFEKT</span><span class="pairing-detail">ZU CHICKEN NUGGETS</span><span class="pairing-detail">UND POMMES FRITES</span></p>
      <p class="line net-weight">NET WT.<br>20 OZ (500g)</p>
    </article>
  </div>

  <!-- LINDO -->
  <div class="label-slot">
    <article class="label">
      <svg class="label-shape" viewBox="0 0 400 725" width="400" height="725" aria-hidden="true">
        <defs>
          <radialGradient id="fill-lindo" cx="50%" cy="45%" r="60%">
            <stop offset="0" stop-color="var(--lindo)"/>
            <stop offset="0.8" stop-color="var(--lindo)"/>
            <stop offset="1" stop-color="#4a0810"/>
          </radialGradient>
        </defs>
        <path fill="var(--tan)" d="M10,120 C30,30 120,0 200,0 C280,0 370,30 390,120 C405,200 380,250 385,300 L385,380 C400,450 400,520 395,560 C385,660 300,725 200,725 C100,725 15,660 5,560 C0,520 0,450 15,380 L15,300 C20,250 -5,200 10,120 Z"/>
        <rect x="20" y="240" width="360" height="158" fill="var(--red)"/>
        <path fill="var(--black)" d="M20,125 C40,40 125,10 200,10 C275,10 360,40 380,125 C392,190 375,240 375,262 C320,295 260,302 200,302 C140,302 80,295 25,262 C25,240 8,190 20,125 Z"/>
        <path fill="none" stroke="var(--tan)" stroke-width="4" d="M65,215 Q200,285 335,215"/>
        <path fill="var(--black)" d="M20,435 C30,398 100,390 200,390 C300,390 370,398 380,435 C395,520 390,590 370,632 C340,692 280,715 200,715 C120,715 60,692 30,632 C10,590 5,520 20,435 Z"/>
        <ellipse cx="200" cy="565" rx="150" ry="138" fill="url(#fill-lindo)"/>
        <circle cx="200" cy="422" r="58" fill="var(--white)"/>
        <circle cx="200" cy="422" r="48" fill="none" stroke="var(--red)" stroke-width="4"/>
      </svg>
      <p class="line sauce-kind">SAUSE</p>
      <p class="line sauce-name">LINDO</p>
      <p class="line brand-name">hubertsen's</p>
      <p class="line pairing"><span class="pairing-lead">PERFEKT</span><span class="pairing-detail">ZU CHICKEN NUGGETS</span><span class="pairing-detail">UND POMMES FRITES</span></p>
      <p class="line net-weight">NET WT.<br>20 OZ (500g)</p>
    </article>
  </div>

  <!-- CHIMICHURRI -->
  <div class="label-slot">
    <article class="label">
      <svg class="label-shape" viewBox="0 0 400 725" width="400" height="725" aria-hidden="true">
        <defs>
          <radialGradient id="fill-chimi" cx="50%" cy="45%" r="60%">
            <stop offset="0" stop-color="var(--chimi)"/>
            <stop offset="0.8" stop-color="var(--chimi)"/>
            <stop offset="1" stop-color="#06361c"/>
          </radialGradient>
        </defs>
        <path fill="var(--tan)" d="M10,120 C30,30 120,0 200,0 C280,0 370,30 390,120 C405,200 380,250 385,300 L385,380 C400,450 400,520 395,560 C385,660 300,725 200,725 C100,725 15,660 5,560 C0,520 0,450 15,380 L15,300 C20,250 -5,200 10,120 Z"/>
        <rect x="20" y="240" width="360" height="158" fill="var(--red)"/>
        <path fill="var(--black)" d="M20,125 C40,40 125,10 200,10 C275,10 360,40 380,125 C392,190 375,240 375,262 C320,295 260,302 200,302 C140,302 80,295 25,262 C25,240 8,190 20,125 Z"/>
        <path fill="none" stroke="var(--tan)" stroke-width="4" d="M65,215 Q200,285 335,215"/>
        <path fill="var(--black)" d="M20,435 C30,398 100,390 200,390 C300,390 370,398 380,435 C395,520 390,590 370,632 C340,692 280,715 200,715 C120,715 60,692 30,632 C10,590 5,520 20,435 Z"/>
        <ellipse cx="200" cy="565" rx="150" ry="138" fill="url(#fill-chimi)"/>
        <circle cx="200" cy="422" r="58" fill="var(--white)"/>
        <circle cx="200" cy="422" r="48" fill="none" stroke="var(--red)" stroke-width="4"/>
      </svg>
      <p class="line sauce-kind">SAUSE</p>
      <p class="line sauce-name sauce-name--mono">CHIMI<br>CHURRI</p>
      <p class="line brand-name">hubertsen's</p>
      <p class="line pairing"><span class="pairing-lead">PERFEKT</span><span class="pairing-detail">ZU CHICKEN NUGGETS</span><span class="pairing-detail">UND POMMES FRITES</span></p>
      <p class="line net-weight">NET WT.<br>20 OZ (500g)</p>
    </article>
  </div>

</main>
</body>
</html>
```